Website Performance Testing eBook for the software testing industry

Overview:
I would like an ebook/whitepaper designed. This ebook will be digital published on my website as a lead generation piece. The purpose is to give high level tips on what to look for and things to think about when working on a website performance testing project.
The ebook also demonstrates our expertise and knowledge on the topic.
Topic:
This is an ebook on software testing. Specifically, website performance testing.
About Veltrano:
Veltrano Solutions is an outsourcing development and software testing firm, and we provide expert services for application development, testing and data analytics. We extend our clients’ software testing capabilities with on-demand technical expertise. Our quality assurance resources work as part of our clients’ teams to help test applications on time and within budget.
Our model is designed to allocate the right mix of local and offshore resources in order to optimize expertise, speed and cost. We provide the ability to quickly add specialty skills to our client’s development team without them incurring long-term costs. The result is far better management of resource capacities and outcomes.
Background on our branding and previous pieces:
I have included a few of our previous ebooks and whitepapers. I like the look and feel of these pieces, however we have made updates to our brand guidelines since them, so the new brand guidelines will need to be incorporated, and I'd like to refresh/update what we have done in the past.
Refer to our website for an idea of our look and feel. This page is one of our newer sections and would be a good reference:
http://www.veltranosol.example/data-analytics/
Tone and feel:
- The look and feel should be professional, clean and polished.
- I like good use of whitespace.
- I would prefer to keep stock photography of people to a minimum. Any images should add to the content and be relevant to the content.
(Also, I uploaded some InDesign files in case you wanted to refer to those assets, but I didn't include the Links folder because they were too big. If there's anything you more you need, let me know)
Target Market(s)
Audience:
The audience is senior Quality Assurance and Software Testing professionals.
- 30-45 years old
- Technical mindset
- Interested in learning
Titles include
- QA Lead
- QA Manager
- QA Director
- Director or VP of Development
- QA Automation Engineer
Our customers are medium to large sized companies. Many are software companies, but many are also enterprises in all almost all industries.

```html
<!DOCTYPE html>
<html lang="en">
<head>
<meta charset="utf-8">
<title>Website Performance Testing Approach</title>
<link rel="stylesheet" href="https://fonts.googleapis.com/css2?family=Open+Sans:wght@300;400&display=swap">
<style>
  :root {
    --brand-red: #e0352b;
    --text-grey: #58595b;
    --rule-grey: #c9c9c9;
    --paper: #ffffff;
    --band-dark: #3f3a39;
    --band-mid: #8a5a50;
    --band-red: #d9432f;
  }
  * { margin: 0; padding: 0; box-sizing: border-box; }
  html, body { width: 927px; height: 1200px; overflow: hidden; background: var(--paper); }
  body { font-family: "Open Sans", Arial, sans-serif; color: var(--text-grey); }
  .page { position: relative; width: 927px; height: 1200px; }

  .running-head {
    position: absolute; left: 54px; top: 73px;
    font-size: 13px; font-weight: 400; color: var(--text-grey);
  }
  .brand-name {
    position: absolute; right: 66px; top: 62px;
    font-size: 26px; font-weight: 400; color: var(--brand-red); letter-spacing: 0.2px;
  }
  .head-rule {
    position: absolute; left: 54px; top: 108px; width: 818px; height: 1px;
    background: var(--rule-grey);
  }

  .section-title {
    position: absolute; left: 98px; top: 166px; height: 106px;
    border-left: 2px solid var(--brand-red);
    padding-left: 27px; padding-top: 14px;
    font-size: 36px; line-height: 38px; font-weight: 300;
    color: var(--brand-red); text-transform: uppercase;
  }

  .body-copy {
    position: absolute; left: 109px; width: 712px;
    font-size: 15px; line-height: 21.2px; font-weight: 400; color: var(--text-grey);
  }
  .p1 { top: 322px; }
  .p2 { top: 459px; }
  .p3 { top: 622px; }
  .p4 { top: 759px; }

  .photo-band {
    position: absolute; left: 0; top: 926px; width: 927px; height: 154px;
    background: linear-gradient(90deg, var(--band-dark) 0%, #5e4a46 35%, var(--band-mid) 60%, var(--band-red) 100%);
  }

  .page-number {
    position: absolute; left: 817px; top: 1123px;
    font-size: 16px; font-weight: 400; color: var(--brand-red);
  }
</style>
</head>
<body>
  <div class="page">
    <div class="running-head">Website Performance Testing</div>
    <div class="brand-name">Veltrano</div>
    <div class="head-rule"></div>

    <h1 class="section-title">Website Performance Testing<br>Approach</h1>

    <p class="body-copy p1">When designing your web performance testing, use a logical approach that gradually narrows down on defects in design, development and deployment. Start with a clear set of objectives and measurable criteria for what your performance tests are to accomplish. Otherwise, you can waste effort testing the wrong things in the wrong places plus be unaware when the test effort is losing effectiveness.</p>

    <p class="body-copy p2">Plan to start performance testing as early as possible in your development cycle to harvest the low-hanging fruit such as major imbalances in the software’s implementation. If possible, engage developers in the early stages of testing. Get them into the habit of examining performance, load and stress results as soon as they become available, so code changes are not delayed and subsequent testing is tweaked effectively with developer input.</p>

    <p class="body-copy p3">To quick-start your testing effort, it helps to focus your testing and optimization efforts on the most-used or high-impact pages based on the percentage of traffic they receive, which you can determine using analysis tools or examining logs. This enables more efficient use of testing resources while deferring changes for rarely visited pages with minor impact on the customer experience.</p>

    <p class="body-copy p4">Finally, regularly review the following do’s and don’ts of website performance testing, especially with regard to cloud-based testing. This will help ensure you are receiving the full benefits of the cloud and that your testing aligns more closely to the conditions of your site when it goes live.</p>

    <div class="photo-band" role="img" aria-label="Tinted photo of a web analytics dashboard showing a traffic sources pie chart"></div>

    <div class="page-number">3</div>
  </div>
</body>
</html>
```